Wirenexa

I'm looking to much improve our current website wirenexa.com
Updates

Low design quality

Target Market(s)

Commercial clients (Not-Residentials)

Industry/Entity Type

Office buildings and Industrial clients

Coding

Coded - Design and coding required

Number of Pages Required

5+ page

Requirements
Must have
• Very professional structured low voltage cabling projects for Wi-Fi, Audio/Video conference rooms, Access Control systems, CCTV.

```html
<!DOCTYPE html>
<html lang="en">
<head>
<meta charset="utf-8">
<title>Wirenexa — Professional Low Voltage Cabling Solutions</title>
<link href="https://fonts.googleapis.com/css2?family=Rajdhani:wght@600;700&family=Inter:wght@400;500;600;700&display=swap" rel="stylesheet">
<style>
:root{
  --red:#e3283b;
  --red-dark:#c81e30;
  --red-soft:#fde8ea;
  --ink:#121212;
  --text:#4a4a52;
  --muted:#8a8a94;
  --line:#ececef;
  --bg-soft:#f6f5f7;
  --white:#fff;
}
*{box-sizing:border-box;margin:0;padding:0}
html,body{width:1200px;height:4655px;overflow:hidden}
body{font-family:'Inter',sans-serif;color:var(--text);background:var(--white);position:relative}
.h{font-family:'Rajdhani',sans-serif;color:var(--ink);font-weight:700}
.red{color:var(--red)}
.wrap{position:absolute;left:103px;width:992px}
section,header,footer{position:absolute;left:0;width:1200px}
.btn{display:inline-flex;align-items:center;gap:8px;height:48px;padding:0 30px;border-radius:4px;font-size:13px;font-weight:600;text-decoration:none;white-space:nowrap}
.btn-red{background:var(--red);color:#fff;box-shadow:0 6px 16px rgba(227,40,59,.28)}
.btn-ghost{background:#fff;color:var(--ink);border:1px solid var(--line)}
.label{font-size:10px;letter-spacing:2.4px;font-weight:600;color:var(--red);text-transform:uppercase;display:flex;align-items:center;gap:8px}
.label::before{content:"";width:18px;height:1.5px;background:var(--red)}
.label.center{justify-content:center}

/* header */
.nav{top:0;height:64px;background:#fff;border-bottom:1px solid var(--line)}
.logo{position:absolute;display:flex;align-items:center;gap:6px;font-family:'Rajdhani',sans-serif;font-weight:700;font-size:24px;color:var(--ink)}
.logo i{width:16px;height:16px;background:var(--red);display:block}
.nav .logo{left:103px;top:18px}
.nav ul{position:absolute;left:464px;top:23px;display:flex;gap:28px;list-style:none;font-size:12px;font-weight:500;color:var(--ink)}
.nav ul li.active{color:var(--red);border-bottom:2px solid var(--red);padding-bottom:4px}
.nav .mode{position:absolute;left:834px;top:16px;width:30px;height:30px;border-radius:6px;background:var(--bg-soft);display:flex;align-items:center;justify-content:center}
.nav .phone{position:absolute;left:882px;top:24px;font-size:12px;font-weight:500;color:var(--ink);display:flex;gap:6px;align-items:center}
.nav .btn{position:absolute;left:996px;top:14px;height:34px;padding:0 18px;font-size:11px}

/* hero */
.hero{top:64px;height:686px;background:radial-gradient(circle at 88% 15%,rgba(227,40,59,.18),transparent 35%),radial-gradient(circle at 15% 75%,rgba(227,40,59,.1),transparent 30%),linear-gradient(180deg,#eff0f3,#f6f4f6);overflow:hidden}
.hero .grid{position:absolute;inset:0;background-image:linear-gradient(rgba(0,0,0,.035) 1px,transparent 1px),linear-gradient(90deg,rgba(0,0,0,.035) 1px,transparent 1px);background-size:40px 40px}
.hero .inner{position:absolute;left:334px;top:81px;width:560px}
.badge{display:inline-flex;align-items:center;gap:8px;height:30px;padding:0 16px;border:1px solid #f2a9b1;background:var(--red-soft);border-radius:15px;font-size:10px;font-weight:600;color:var(--red)}
.badge::before{content:"";width:5px;height:5px;border-radius:50%;background:var(--red)}
.hero h1{font-size:66px;line-height:72px;margin-top:26px;letter-spacing:.3px}
.hero p{font-size:14px;line-height:25px;margin-top:18px;width:490px;color:#45454d}
.hero .actions{margin-top:32px;display:flex;gap:14px}
.hero .checks{margin-top:32px;display:flex;gap:18px;font-size:10px;color:var(--muted);white-space:nowrap}
.hero .checks span::before{content:"✓";color:var(--red);margin-right:6px}
.hero .dot{position:absolute;left:597px;top:651px;width:6px;height:6px;border-radius:50%;background:var(--red)}

.clients{top:750px;height:45px;background:#fff;display:flex;align-items:center;justify-content:center;gap:48px;font-size:10px;font-weight:600;letter-spacing:1.6px;color:#9b9ba3;white-space:nowrap;overflow:hidden}
.clients span{flex:none}
.clients span:first-child,.clients span:last-child{color:#d4d4d8}

/* stats */
.stats{top:795px;height:311px;background:var(--bg-soft)}
.stats .wrap{top:69px;height:177px;display:grid;grid-template-columns:repeat(4,1fr);background:#fff;border-radius:10px;overflow:hidden;box-shadow:0 4px 20px rgba(0,0,0,.04)}
.stat{text-align:center;padding-top:38px;border-right:1px solid var(--line)}
.stat:last-child{border:0}
.stat b{display:block;font-family:'Rajdhani',sans-serif;font-size:42px;color:var(--red);line-height:1}
.stat strong{display:block;font-size:12px;color:var(--ink);font-weight:600;margin-top:14px}
.stat small{display:block;font-size:10px;color:var(--muted);margin-top:8px}

/* services */
.services{top:1106px;height:1290px;background:#fff}
.sec-head{position:absolute;left:103px;top:97px}
.sec-head h2{font-size:38px;line-height:45px;margin-top:22px}
.sec-head p{font-size:13px;line-height:24px;width:470px;margin-top:22px}
.cards{position:absolute;left:103px;top:347px;width:992px;display:grid;grid-template-columns:repeat(3,1fr);gap:22px 22px}
.card{border:1px solid var(--line);border-radius:8px;overflow:hidden;background:#fff;height:383px}
.card.short{height:365px}
.card .media{height:163px;position:relative}
.card .media::after{content:"";position:absolute;inset:0;background:linear-gradient(180deg,transparent 55%,#fff)}
.card .tag{position:absolute;right:10px;top:10px;z-index:1;background:var(--red);color:#fff;font-size:9px;font-weight:600;padding:4px 9px;border-radius:10px}
.card .body{padding:10px 20px}
.ico{width:38px;height:38px;border-radius:7px;background:var(--red-soft);display:flex;align-items:center;justify-content:center}
.card h3{font-family:'Rajdhani',sans-serif;font-size:15px;color:var(--ink);margin-top:16px}
.card p{font-size:11px;line-height:19px;margin-top:10px;color:#5a5a62}
.card a{display:inline-block;margin-top:12px;font-size:11px;font-weight:600;color:var(--red);text-decoration:none}
.services .more{position:absolute;left:503px;top:1156px;height:49px;padding:0 30px;border:1px solid var(--line);border-radius:4px;font-size:13px;font-weight:600;color:var(--ink);display:flex;align-items:center;gap:8px}
.m1{background:linear-gradient(135deg,#59636f,#9aa5b1 60%,#c9d0d6)}
.m2{background:linear-gradient(160deg,#8c9fb2,#c5d2de 60%,#e4e9ee)}
.m3{background:linear-gradient(135deg,#4a5b74,#8ea2bb 60%,#d1dae3)}
.m4{background:linear-gradient(135deg,#6d6259,#a99e92 55%,#d6d0ca)}
.m5{background:linear-gradient(160deg,#3f4a44,#7e8a80 55%,#c2c7c3)}
.m6{background:linear-gradient(135deg,#0f2a5a,#2e5aa8 55%,#9db4d8)}

/* why */
.why{top:2396px;height:604px;background:radial-gradient(circle at 62% 30%,rgba(227,40,59,.14),transparent 35%),var(--bg-soft);overflow:hidden}
.why .grid{position:absolute;inset:0;background-image:linear-gradient(rgba(0,0,0,.03) 1px,transparent 1px),linear-gradient(90deg,rgba(0,0,0,.03) 1px,transparent 1px);background-size:40px 40px}
.why .left{position:absolute;left:103px;top:85px;width:470px}
.why h2{font-size:38px;line-height:46px;margin-top:16px}
.why .left p{font-size:13px;line-height:24px;margin-top:20px}
.why ul{list-style:none;margin-top:26px;font-size:11px;font-weight:500;color:#333}
.why li{height:27.5px}
.why li::before{content:"✓";color:var(--red);margin-right:9px}
.why .actions{display:flex;gap:10px;margin-top:14px}
.why .actions .btn{height:45px;padding:0 24px;font-size:12px}
.why .actions .btn-ghost{color:var(--red)}
.why .tiles{position:absolute;left:633px;top:108px;width:462px;display:grid;grid-template-columns:1fr 1fr;gap:14px}
.tile{background:#fff;border-radius:6px;height:185px;padding:24px 20px;box-shadow:0 4px 18px rgba(0,0,0,.05)}
.tile h4{font-size:11px;color:var(--ink);font-weight:700;margin-top:16px}
.tile p{font-size:10px;line-height:17px;margin-top:8px;color:#5a5a62}

/* process */
.process{top:3000px;height:556px;background:#fff;text-align:center}
.process .label{position:absolute;left:0;right:0;top:90px}
.process h2{position:absolute;left:0;right:0;top:118px;font-size:40px}
.process .lead{position:absolute;left:350px;width:500px;top:190px;font-size:13px;line-height:24px}
.steps{position:absolute;left:103px;top:276px;width:992px;display:grid;grid-template-columns:repeat(4,1fr);gap:22px}
.step{border:1px solid var(--line);border-radius:6px;height:194px;padding-top:30px;position:relative}
.step:last-child{height:180px}
.step:not(:last-child)::after{content:"";position:absolute;right:-20px;top:97px;width:18px;height:1.5px;background:#f0a2ab}
.step b{font-family:'Rajdhani',sans-serif;font-size:38px;color:var(--red);display:block;line-height:1}
.step h4{font-family:'Rajdhani',sans-serif;font-size:14px;color:var(--ink);margin-top:20px}
.step p{font-size:10.5px;line-height:19px;margin:10px auto 0;width:185px}

/* cta */
.cta{top:3556px;height:570px;background:linear-gradient(180deg,#fff,#f6f2f4)}
.cta .box{position:absolute;left:103px;top:85px;width:992px;height:400px;border:1px solid #f3c2c8;border-radius:22px;background:radial-gradient(circle at 50% 40%,#fff 0,#fbe9ec 70%);text-align:center}
.cta .label{margin-top:80px}
.cta h2{font-size:38px;line-height:44px;margin-top:16px}
.cta p{font-size:13px;line-height:22px;width:420px;margin:20px auto 0}
.cta .actions{display:flex;gap:14px;justify-content:center;margin-top:30px}
.cta .actions .btn-ghost{background:transparent;border:0}

.bar{top:4126px;height:144px;background:#f6f3f5;border-top:1px solid var(--line)}
.bar h3{position:absolute;left:103px;top:48px;font-size:21px}
.bar p{position:absolute;left:103px;top:84px;font-size:12px}
.bar .actions{position:absolute;right:105px;top:50px;display:flex;gap:12px}
.bar .btn{height:44px;padding:0 22px;font-size:12px}
.bar .btn-ghost{border-color:#f0b3ba}

/* footer */
.foot{top:4270px;height:385px;background:#fff}
.foot .logo{left:103px;top:58px}
.foot .about{position:absolute;left:103px;top:108px;width:280px;font-size:11px;line-height:20px}
.socials{position:absolute;left:103px;top:192px;display:flex;gap:10px}
.socials span{width:24px;height:24px;border:1px solid var(--line);border-radius:5px;display:flex;align-items:center;justify-content:center}
.socials span i{width:8px;height:8px;background:#aaa;border-radius:2px}
.fcol{position:absolute;top:60px}
.fcol h5{font-size:10px;letter-spacing:1.6px;color:var(--ink);font-weight:700}
.fcol ul{list-style:none;margin-top:26px;font-size:11px;line-height:27px;padding-left:14px}
.fcol.contact ul{padding-left:0;line-height:16px}
.fcol.contact li{display:flex;gap:10px;margin-bottom:14px;font-size:10.5px}
.fcol.contact strong{color:var(--ink);font-size:10px}
.copy{position:absolute;left:103px;right:105px;top:330px;border-top:1px solid var(--line);padding-top:24px;display:flex;justify-content:space-between;font-size:10px}
</style>
</head>
<body>

<header class="nav">
  <div class="logo"><i></i>Wirenexa</div>
  <ul><li class="active">Home</li><li>About</li><li>Services</li><li>Projects</li><li>Contact</li></ul>
  <div class="mode"><svg width="13" height="13" viewBox="0 0 24 24" fill="none" stroke="#333" stroke-width="2"><path d="M21 13A9 9 0 1 1 11 3a7 7 0 0 0 10 10z"/></svg></div>
  <div class="phone"><svg width="12" height="12" viewBox="0 0 24 24" fill="none" stroke="#333" stroke-width="2"><path d="M22 17v3a2 2 0 0 1-2 2A19 19 0 0 1 2 4a2 2 0 0 1 2-2h3l2 5-2.5 1.5a11 11 0 0 0 6 6L15 12l5 2z"/></svg>888-555-0142</div>
  <a class="btn btn-red">Get a Quote</a>
</header>

<section class="hero">
  <div class="grid"></div>
  <div class="inner">
    <span class="badge">Trusted IT Infrastructure Partner Since 1994</span>
    <h1 class="h">Professional<br><span class="red">Low Voltage</span><br>Cabling Solutions</h1>
    <p>Wirenexa delivers expert structured cabling, Wi-Fi, Audio/Video, Access Control, and CCTV for commercial offices, warehousing, and small to mid-size businesses in Virginia, DC, Maryland &amp; nationwide.</p>
    <div class="actions">
      <a class="btn btn-red">Get a Free Quote →</a>
      <a class="btn btn-ghost">Explore Services</a>
    </div>
    <div class="checks"><span>CAT6/CAT7 Certified</span><span>Low Voltage Permits</span><span>Nationwide Coverage</span><span>Commercial &amp; Gov</span></div>
  </div>
  <div class="dot"></div>
</section>

<section class="clients">
  <span>CINEMAS</span><span>DESKWELL</span><span>CIVIC AGENCY</span><span>CORPORATE OFFICES</span><span>WAREHOUSES</span><span>RETAIL PROPERTIES</span><span>GOVERNMENT</span><span>NORTHPOINT HEALTH</span><span>MARQUEE CINEMAS</span>
</section>

<section class="stats">
  <div class="wrap">
    <div class="stat"><b>30+</b><strong>Years of Experience</strong><small>Founded in 1994</small></div>
    <div class="stat"><b>500+</b><strong>Projects Completed</strong><small>Nationwide</small></div>
    <div class="stat"><b>50</b><strong>States Served</strong><small>Across the US</small></div>
    <div class="stat"><b>99%</b><strong>Client Satisfaction</strong><small>Long-term partnerships</small></div>
  </div>
</section>

<section class="services">
  <div class="sec-head">
    <div class="label">What we do</div>
    <h2 class="h">Complete Low Voltage<br><span class="red">Cabling Solutions</span></h2>
    <p>From copper CAT6/CAT7 to fiber optic and full security systems — we deliver end-to-end infrastructure for commercial offices, warehouses, and corporate facilities.</p>
  </div>
  <div class="cards">
    <article class="card short"><div class="media m1" role="img" aria-label="Technician working on structured cabling at a patch panel"><span class="tag">Core Service</span></div><div class="body"><div class="ico"><svg width="16" height="16" viewBox="0 0 24 24" fill="none" stroke="#e3283b" stroke-width="2"><rect x="3" y="4" width="18" height="7" rx="1"/><rect x="3" y="13" width="18" height="7" rx="1"/></svg></div><h3>Structured Cabling</h3><p>CAT6 &amp; CAT7 copper cabling and fiber optic installations for seamless enterprise connectivity.</p><a>Learn More ›</a></div></article>
    <article class="card"><div class="media m2" role="img" aria-label="Open office ceiling with wireless access points"><span class="tag">Wireless</span></div><div class="body"><div class="ico"><svg width="16" height="16" viewBox="0 0 24 24" fill="none" stroke="#e3283b" stroke-width="2"><path d="M2 9a15 15 0 0 1 20 0M5 13a10 10 0 0 1 14 0M8.5 16.5a5 5 0 0 1 7 0"/><circle cx="12" cy="20" r="1"/></svg></div><h3>Wi-Fi Solutions</h3><p>Enterprise-grade wireless deployments engineered for maximum coverage and performance.</p><a>Learn More ›</a></div></article>
    <article class="card short"><div class="media m3" role="img" aria-label="Conference room with video wall and meeting table"><span class="tag">AV Integration</span></div><div class="body"><div class="ico"><svg width="16" height="16" viewBox="0 0 24 24" fill="none" stroke="#e3283b" stroke-width="2"><rect x="3" y="4" width="18" height="12" rx="1"/><path d="M8 20h8M12 16v4"/></svg></div><h3>Audio/Video Systems</h3><p>Professional AV integration for conference rooms, boardrooms, and collaboration spaces.</p><a>Learn More ›</a></div></article>
    <article class="card short"><div class="media m4" role="img" aria-label="Staff member using a badge reader at an office entrance"><span class="tag">Security</span></div><div class="body"><div class="ico"><svg width="16" height="16" viewBox="0 0 24 24" fill="none" stroke="#e3283b" stroke-width="2"><path d="M12 3l8 3v6c0 5-4 8-8 9-4-1-8-4-8-9V6z"/></svg></div><h3>Access Control</h3><p>Intelligent electronic access control systems to secure your facilities and manage entry.</p><a>Learn More ›</a></div></article>
    <article class="card short"><div class="media m5" role="img" aria-label="Security monitoring room with camera feeds"><span class="tag">Security</span></div><div class="body"><div class="ico"><svg width="16" height="16" viewBox="0 0 24 24" fill="none" stroke="#e3283b" stroke-width="2"><rect x="3" y="7" width="18" height="13" rx="2"/><circle cx="12" cy="13" r="3.5"/><path d="M9 7l1.5-3h3L15 7"/></svg></div><h3>CCTV &amp; Surveillance</h3><p>High-definition IP camera systems with remote monitoring for comprehensive site security.</p><a>Learn More ›</a></div></article>
    <article class="card short"><div class="media m6" role="img" aria-label="Network rack with organized cable management"><span class="tag">Infrastructure</span></div><div class="body"><div class="ico"><svg width="16" height="16" viewBox="0 0 24 24" fill="none" stroke="#e3283b" stroke-width="2"><rect x="4" y="4" width="7" height="7"/><rect x="13" y="4" width="7" height="7"/><rect x="4" y="13" width="7" height="7"/><rect x="13" y="13" width="7" height="7"/></svg></div><h3>IDF/MDF &amp; Racking</h3><p>Professional rack installation and data room build-outs with meticulous cable management.</p><a>Learn More ›</a></div></article>
  </div>
  <div class="more">View All Services →</div>
</section>

<section class="why">
  <div class="grid"></div>
  <div class="left">
    <div class="label">Why Wirenexa</div>
    <h2 class="h">The <span class="red">Trusted Partner</span><br>for IT Infrastructure</h2>
    <p>With decades of experience and hundreds of projects completed, we bring the expertise and commitment your business deserves.</p>
    <ul><li>CAT6 &amp; CAT7 Copper Cabling</li><li>Single &amp; Multimode Fiber Optic</li><li>Low Voltage Permits</li><li>Certified Cabling Professionals</li><li>Full Project Documentation</li><li>Post-installation Support</li></ul>
    <div class="actions"><a class="btn btn-red">About Wirenexa →</a><a class="btn btn-ghost">✆ Call Now</a></div>
  </div>
  <div class="tiles">
    <div class="tile"><svg width="20" height="20" viewBox="0 0 24 24" fill="none" stroke="#d99a1e" stroke-width="2"><path d="M7 4h10v5a5 5 0 0 1-10 0zM12 14v4M8 20h8"/></svg><h4>Decades of Expertise</h4><p>Since 1994, our seasoned professionals deliver efficient, results-oriented cabling solutions tailored to your needs.</p></div>
    <div class="tile"><svg width="20" height="20" viewBox="0 0 24 24" fill="#f2b233"><path d="M12 21s-8-5-8-11a4.5 4.5 0 0 1 8-2.8A4.5 4.5 0 0 1 20 10c0 6-8 11-8 11z"/></svg><h4>White-Glove Service</h4><p>Customer satisfaction is our top priority. We deliver top-notch support and professionalism from planning to completion.</p></div>
    <div class="tile"><svg width="20" height="20" viewBox="0 0 24 24" fill="none" stroke="#3a8fd6" stroke-width="2"><circle cx="12" cy="12" r="9"/><path d="M3 12h18M12 3c3 3 3 15 0 18M12 3c-3 3-3 15 0 18"/></svg><h4>Nationwide Coverage</h4><p>We've successfully supported hundreds of companies nationwide, bringing consistent quality to every project.</p></div>
    <div class="tile"><svg width="20" height="20" viewBox="0 0 24 24" fill="none" stroke="#555" stroke-width="2"><path d="M3 9l9-5 9 5M5 10v8M10 10v8M14 10v8M19 10v8M3 20h18"/></svg><h4>Commercial &amp; Gov Expertise</h4><p>Trusted by Northpoint Health, Marquee Cinemas, Deskwell, Civic Agency, and many leading organizations across sectors.</p></div>
  </div>
</section>

<section class="process">
  <div class="label center">How we work</div>
  <h2 class="h">Our Proven <span class="red">4-Step</span> Process</h2>
  <p class="lead">A structured approach that delivers consistent, high-quality results every time.</p>
  <div class="steps">
    <div class="step"><b>01</b><h4>Assessment</h4><p>We analyze your site, requirements, and infrastructure needs.</p></div>
    <div class="step"><b>02</b><h4>Design</h4><p>Custom cabling blueprint designed for efficiency and scalability.</p></div>
    <div class="step"><b>03</b><h4>Installation</h4><p>Expert installation with certified technicians and premium materials.</p></div>
    <div class="step"><b>04</b><h4>Certification</h4><p>Full testing, documentation, and system certification delivered.</p></div>
  </div>
</section>

<section class="cta">
  <div class="box">
    <div class="label center">Get started today</div>
    <h2 class="h">Ready to Build a Smarter<br>Infrastructure?</h2>
    <p>Contact our team for a free consultation and custom quote tailored to your project.</p>
    <div class="actions"><a class="btn btn-red">Request Free Quote →</a><a class="btn btn-ghost">✆ 888-555-0142</a></div>
  </div>
</section>

<section class="bar">
  <h3 class="h">Ready to Upgrade Your Infrastructure?</h3>
  <p>Let's build a smarter, more connected workspace together.</p>
  <div class="actions"><a class="btn btn-ghost">✆ 888-555-0142</a><a class="btn btn-red">Request a Quote</a></div>
</section>

<footer class="foot">
  <div class="logo"><i></i>Wirenexa</div>
  <p class="about">Leading infrastructure cabling company dedicated to building, managing, securing, and supporting IT infrastructure since 1994.</p>
  <div class="socials"><span><i></i></span><span><i></i></span><span><i></i></span></div>
  <div class="fcol" style="left:423px"><h5>QUICK LINKS</h5><ul><li>Home</li><li>About Us</li><li>Services</li><li>Projects</li><li>Contact</li><li>Get a Quote</li></ul></div>
  <div class="fcol" style="left:638px"><h5>OUR SERVICES</h5><ul><li>Structured Cabling</li><li>Wi-Fi Solutions</li><li>Audio/Video Systems</li><li>Access Control</li><li>CCTV &amp; Security</li><li>IDF/MDF &amp; Racking</li></ul></div>
  <div class="fcol contact" style="left:851px"><h5>CONTACT US</h5><ul>
    <li><span class="red">⌖</span><div><strong>MAIN OFFICE (VA)</strong><br>4120 Harlow Pkwy, Suite 210<br>Vienna, VA 22182</div></li>
    <li><span class="red">⌖</span><div><strong>REGIONAL (MD)</strong><br>5300 Ridgeline Ave, Suite 300<br>Bethesda, MD 20817</div></li>
    <li><span class="red">✆</span><div>888-555-0142 (National)<br>703-555-0190 (Local)</div></li>
    <li><span class="red">✉</span><div>sales@wirenexa.com</div></li>
  </ul></div>
  <div class="copy"><span>© 2026 Wirenexa. All rights reserved.</span><span>Serving Virginia • Maryland • Washington DC &amp; Nationwide</span></div>
</footer>

</body>
</html>
```